Small business services company needs a flyer designed

We need a flyer designed for a small building services company who has multiple roles ie- Roof, gutter and pressure cleaning, small building maintenance and garden cleanups. The company is based in Far North Queensland (Australia) where it is a tropical climate with lots of trees and green areas.

I want the colours to be based on the Logo and business card colours which will be added.

The flyer will need to be changeable so I can create monthly specials ie- Roof Cleaning Special, Gutter Cleaning Special or Pressure Cleaning special.

The roles of the business will be as stated on the attached business card.

Good evening all designers, please find below an update for you all, I hope it may answer some questions you have.

'd like the flyer to be DL size and at present I don't have any photo's. But i'd be happy for you to source some from google. The pictures I'd like would be of gutter cleaning from a ladder, pressure washing roofs & driveways with the large round "flat surface cleaners". Possibly have split pictures of the pressure cleaning to show before and after. 
Far North Queensland is a very tropical environment that has lots of palm trees and rain forest. The climate is usually 30+ degrees C. Incorporating those colours with the logo colours I'd like. 

Hello all designers.

I have just uploaded some of my own job pictures. There is a before and an after picture. If you source any other pictures, I'd like to see a flat surface/ spinmaster cleaner in operation, either on a roof or a driveway.

My goal is for a single sided flyer with all the details from my business card to be on the flyer. 

Please remember the climate in my area is very tropical and usually 30+ degrees C. Never cold or snowing. So please have pictures to reflect.

Thanks for the designs.
Regards,Darren

Reason: hi all designers. I have extended the deadline by 3 days to accommodate all the designers who have only recently accepted the brief nest invites. I have had a lot of declines and want the best designs I can choice from. This is no reflection of the calibre of the designs I have already received. I look forward to seeing all the updates and new designs. Regards, Darren

Home owners who take pride in the street appeal of their homes, or to add value to their selling price when a house goes on the sales market.

Building

```html
<!DOCTYPE html>
<html lang="en">
<head>
<meta charset="utf-8">
<title>Uplift Roof, Gutter &amp; Pressure Cleaning Flyer</title>
<link rel="stylesheet" href="https://fonts.googleapis.com/css2?family=Roboto+Condensed:wght@700&family=Source+Sans+3:wght@400;600;700&family=Arimo:wght@700&display=swap">
<style>
  :root {
    --teal: #19a897;
    --teal-dark: #138a7c;
    --ink: #1a1a1a;
    --brand-blue: #2b3a96;
    --white: #ffffff;
    --backdrop-inner: #5a5a5a;
    --backdrop-outer: #2e2e2e;
    --badge-top: #1aa593;
    --badge-bottom: #5d6e6c;
  }
  * { margin: 0; padding: 0; box-sizing: border-box; }
  html, body { width: 1200px; height: 999px; overflow: hidden; }
  body {
    position: relative;
    background: radial-gradient(ellipse at center, var(--backdrop-inner) 0%, var(--backdrop-outer) 100%);
    font-family: "Source Sans 3", "Myriad Pro", sans-serif;
  }
  .flyer {
    position: absolute;
    left: 391px; top: 56px;
    width: 418px; height: 886px;
    background: var(--white);
    overflow: hidden;
  }
  .top-band { position: absolute; left: 0; top: 0; width: 100%; height: 22px; background: var(--teal); }
  .brand {
    position: absolute; left: 0; top: 22px; width: 100%; height: 135px;
    display: flex; flex-direction: column; align-items: center; justify-content: center;
  }
  .brand-row { display: flex; align-items: center; gap: 14px; }
  .brand-mark { width: 34px; height: 34px; background: var(--brand-blue); }
  .brand-name {
    font-family: "Roboto Condensed", sans-serif; font-weight: 700;
    font-size: 58px; line-height: 1; color: var(--brand-blue); letter-spacing: 1px;
  }
  .brand-tagline {
    margin-top: 6px; font-size: 10px; font-weight: 700; color: var(--brand-blue);
    text-transform: uppercase; letter-spacing: 0.3px;
  }
  .brand-call { margin-top: 2px; font-size: 13px; font-weight: 700; color: var(--teal-dark); }
  .photo-stripe { position: absolute; left: 0; top: 157px; width: 100%; height: 7px; background: var(--teal); }
  .photo {
    position: absolute; left: 0; top: 164px; width: 100%; height: 261px;
    background: linear-gradient(160deg, #9a8f86 0%, #7d746e 40%, #5d5a57 70%, #6f6b66 100%);
  }
  .photo-divider { position: absolute; left: 0; top: 423px; width: 100%; height: 8px; }
  .badge { position: absolute; left: 251px; top: 418px; width: 162px; height: 162px; }
  .badge-text {
    position: absolute; left: 251px; top: 418px; width: 162px; height: 162px;
    display: flex; flex-direction: column; align-items: center; justify-content: center;
    color: var(--white); text-align: center; line-height: 1.05;
  }
  .badge-percent { font-family: "Arimo", sans-serif; font-size: 26px; }
  .badge-label { font-family: "Arimo", sans-serif; font-size: 20px; }
  .badge-detail { font-size: 14px; line-height: 1.25; }
  .badge-detail.small { font-size: 12.5px; }
  .headline {
    position: absolute; left: 25px; top: 448px;
    font-family: "Roboto Condensed", sans-serif; font-weight: 700;
    font-size: 76px; line-height: 1; color: var(--teal);
  }
  .subhead {
    position: absolute; left: 25px; top: 529px;
    font-size: 21px; line-height: 29px; color: var(--ink);
  }
  .special-pill {
    position: absolute; left: 70px; top: 606px; width: 269px; height: 46px;
    border-radius: 23px; background: var(--teal); color: var(--white);
    font-family: "Roboto Condensed", sans-serif; font-weight: 700; font-size: 29px;
    display: flex; align-items: center; justify-content: center;
  }
  .services {
    position: absolute; left: 0; top: 659px; width: 100%;
    list-style: none; text-align: center; font-size: 18.5px; line-height: 24px; color: var(--ink);
  }
  .sectors-pill {
    position: absolute; left: 19px; top: 746px; width: 380px; height: 33px;
    border-radius: 17px; background: var(--teal); color: var(--white);
    font-weight: 700; font-size: 16px;
    display: flex; align-items: center; justify-content: center;
  }
  .footer {
    position: absolute; left: 0; top: 789px; width: 100%; height: 97px;
    background: var(--teal); color: var(--white); text-align: center;
  }
  .footer-phone { margin-top: 4px; font-family: "Arimo", sans-serif; font-size: 42px; line-height: 48px; }
  .footer-email { margin-top: 6px; font-size: 19px; }
</style>
</head>
<body>
  <main class="flyer">
    <div class="top-band"></div>

    <header class="brand">
      <div class="brand-row">
        <span class="brand-name">UPLIFT</span>
        <span class="brand-mark"></span>
      </div>
      <p class="brand-tagline">Roof, Gutter &amp; Pressure Cleaning Services</p>
      <p class="brand-call">CALL 0400 555 231</p>
    </header>

    <div class="photo-stripe"></div>
    <div class="photo" role="img" aria-label="Worker on a roof pressure cleaning the roof sheets, paved driveway and garden below, ladder against the gutter"></div>
    <svg class="photo-divider" viewBox="0 0 418 8" preserveAspectRatio="none">
      <polygon points="0,2 418,0 418,8 0,8" fill="var(--teal)"/>
    </svg>

    <svg class="badge" viewBox="-81 -81 162 162">
      <defs>
        <linearGradient id="badgeFill" x1="0" y1="0" x2="0" y2="1">
          <stop offset="0" stop-color="var(--badge-top)"/>
          <stop offset="1" stop-color="var(--badge-bottom)"/>
        </linearGradient>
      </defs>
      <polygon fill="url(#badgeFill)" stroke="var(--white)" stroke-width="2"
        points="80,0 67.2,10.6 76.1,24.7 60.6,30.9 64.7,47 48.1,48.1 47,64.7 30.9,60.6 24.7,76.1 10.6,67.2 0,80 -10.6,67.2 -24.7,76.1 -30.9,60.6 -47,64.7 -48.1,48.1 -64.7,47 -60.6,30.9 -76.1,24.7 -67.2,10.6 -80,0 -67.2,-10.6 -76.1,-24.7 -60.6,-30.9 -64.7,-47 -48.1,-48.1 -47,-64.7 -30.9,-60.6 -24.7,-76.1 -10.6,-67.2 0,-80 10.6,-67.2 24.7,-76.1 30.9,-60.6 47,-64.7 48.1,-48.1 64.7,-47 60.6,-30.9 76.1,-24.7 67.2,-10.6"/>
    </svg>
    <div class="badge-text">
      <span class="badge-percent">10%</span>
      <span class="badge-label">Discount</span>
      <span class="badge-detail">for Emergency</span>
      <span class="badge-detail">Services</span>
      <span class="badge-detail small">Defence &amp;</span>
      <span class="badge-detail small">Seniors</span>
    </div>

    <h1 class="headline">UPLIFT</h1>
    <p class="subhead">Roof, Gutter &amp; Pressure<br>Cleaning Service</p>

    <div class="special-pill">GUTTER CLEANING</div>

    <ul class="services">
      <li>Pressure Cleaning-Roof’s, Driveways ets</li>
      <li>Minor Roof, Gutter &amp; Building Maintenance</li>
      <li>Garden Waste Removal &amp; Complex Cleanup</li>
    </ul>

    <div class="sectors-pill">Residential, Commercial &amp; Body Corporate Jobs</div>

    <footer class="footer">
      <p class="footer-phone">0400 555 231</p>
      <p class="footer-email">roofcleaning@mailhub.com.au</p>
    </footer>
  </main>
</body>
</html>
```